Door Hanger Design

I need a design for a door hanger campaign. The door hanger will be 3.5" x 8.5" full color 2 sides. On the first side the emphasis is going to be house painting, exterior and interior. I would really like this to be bold and colorful, I would like to stay away from the standard here is what a painted house looks like.

For the 2nd side I would like the emphasis to be on kitchen and bathroom remodeling. One the front page of our website is a photo of one of our best jobs and if that could be incorporated into side 2 of the door hanger that would be awesome.

The name of our business is Casa Brightwell . Our website is http://casa-brightwell.example/. We don't currently have a company logo that we use.

I have never done this type of project before. So I'm sure I may be leaving some information out. If you need any questions answered please don't hesitate to contact me. They company that is going to print the designs said that I needed "camera ready artwork" and something about high resolution files.

Industry/Entity Type

House

```html
<!DOCTYPE html>
<html lang="en">
<head>
<meta charset="utf-8">
<title>Casa Brightwell – Door Hanger</title>
<link rel="stylesheet" href="https://fonts.googleapis.com/css2?family=Anton&family=Oswald:wght@700&family=PT+Serif&display=swap">
<style>
  :root {
    --stage: #2c3a66;
    --paint-orange: #ff4a1c;
    --paint-blue: #0a6ae0;
    --paint-green: #b2f02c;
    --logo-yellow: #f8f64a;
    --ink: #0d0d0d;
    --wood-light: #c98e4c;
    --wood-dark: #9a5e2a;
    --steel-light: #dcdcdc;
    --steel-dark: #8d8f91;
    --card-white: #ffffff;
    --card-ink: #1c3f8f;
  }
  * { box-sizing: border-box; margin: 0; padding: 0; }
  html, body { width: 1018px; height: 1200px; overflow: hidden; }
  body { background: var(--stage); position: relative; font-family: "Oswald", sans-serif; }

  .hanger {
    position: absolute; top: 45px; width: 432px; height: 1114px; overflow: hidden;
    background: var(--paint-blue);
    box-shadow: 8px 10px 18px rgba(0,0,0,.55);
  }
  .hanger--paint { left: 55px; }
  .hanger--remodel { left: 526px; }

  .paint-band { position: absolute; left: 0; right: 0; }
  .paint-band--top {
    top: 0; height: 330px; background: var(--paint-orange);
    clip-path: polygon(0 0, 100% 0, 100% 290px, 0 320px);
  }
  .paint-band--bottom {
    bottom: 0; height: 390px; background: var(--paint-green);
    clip-path: polygon(0 0, 100% 10px, 100% 100%, 0 100%);
  }

  .brand {
    position: absolute; left: 0; width: 100%; text-align: center;
    font-family: "Anton", sans-serif; font-weight: 400; color: var(--logo-yellow); line-height: 1;
  }
  .hanger--paint .brand { top: 468px; font-size: 92px; }
  .hanger--paint .brand span { display: block; font-size: 58px; margin-top: 6px; }
  .hanger--remodel .brand { top: 262px; left: 40px; width: 170px; font-size: 40px; }
  .hanger--remodel .brand span { display: block; font-size: 26px; margin-top: 2px; }

  .website {
    position: absolute; left: 0; width: 100%; text-align: center;
    font-family: "Oswald", sans-serif; font-weight: 700; color: var(--logo-yellow);
  }
  .hanger--paint .website { top: 652px; font-size: 20px; }
  .hanger--remodel .website { top: 336px; left: 20px; width: 210px; font-size: 13px; }

  .contact { position: absolute; left: 0; width: 100%; text-align: center; color: var(--ink); }
  .contact .owner { font-family: "Anton", sans-serif; font-size: 40px; line-height: 42px; }
  .contact .credentials { font-family: "PT Serif", serif; font-size: 22px; line-height: 30px; margin-top: 4px; }
  .contact .phone { font-family: "Anton", sans-serif; font-size: 38px; line-height: 40px; margin-top: 12px; }
  .contact .email { font-family: "Oswald", sans-serif; font-weight: 700; font-size: 17px; line-height: 24px; margin-top: 4px; }
  .hanger--paint .contact { top: 828px; }
  .hanger--remodel .contact { top: 816px; }

  .payments {
    position: absolute; top: 1019px; width: 278px; height: 77px;
    background: var(--card-white); border: 1px solid #777;
    display: flex; align-items: center; justify-content: space-around; padding: 0 10px;
  }
  .hanger--paint .payments { left: 87px; }
  .hanger--remodel .payments { left: 73px; }
  .payments .card-name {
    display: flex; align-items: center; gap: 4px;
    font-family: "Oswald", sans-serif; font-weight: 700; font-size: 15px; color: var(--card-ink);
  }
  .payments .card-name i { width: 10px; height: 10px; background: var(--card-ink); display: inline-block; }

  .wood-panel {
    position: absolute; left: 0; right: 0; top: 0; height: 390px;
    background: linear-gradient(180deg, var(--wood-light), var(--wood-dark) 55%, var(--wood-light));
    clip-path: polygon(0 0, 100% 0, 100% 352px, 0 385px);
  }
  .kitchen-photo {
    position: absolute; left: 36px; top: 400px; width: 364px; height: 345px;
    background: linear-gradient(160deg, #efe7d6 0%, #c9b79a 35%, #7a3b22 70%, #4d2314 100%);
    transform: rotate(1.5deg);
    box-shadow: 4px 6px 10px rgba(0,0,0,.45);
  }
  .steel-panel {
    position: absolute; left: 0; right: 0; top: 767px; bottom: 0;
    background: linear-gradient(90deg, var(--steel-dark), var(--steel-light) 30%, #b4b6b8 60%, var(--steel-light) 85%, var(--steel-dark));
    border-top: 4px solid #f2f2f2;
  }
</style>
</head>
<body>

<section class="hanger hanger--paint" aria-label="Door hanger side one: house painting">
  <div class="paint-band paint-band--top" role="img" aria-label="Orange paint dripping down over the blue"></div>
  <div class="paint-band paint-band--bottom" role="img" aria-label="Blue paint dripping down into lime green"></div>
  <h1 class="brand">Casa<span>Brightwell</span></h1>
  <p class="website">casa-brightwell.example</p>
  <div class="contact">
    <p class="owner">Marcus Delane</p>
    <p class="credentials">Licensed and Insured</p>
    <p class="phone">904-555-0172</p>
    <p class="email">marcusdelane@example.com</p>
  </div>
  <div class="payments" aria-label="Accepted payment cards">
    <span class="card-name"><i></i>Paxa</span>
    <span class="card-name"><i></i>Orbita</span>
    <span class="card-name"><i></i>Amerin</span>
  </div>
</section>

<section class="hanger hanger--remodel" aria-label="Door hanger side two: kitchen and bathroom remodeling">
  <div class="wood-panel" role="img" aria-label="Warm hardwood floor planks"></div>
  <h2 class="brand">Casa<span>Brightwell</span></h2>
  <p class="website">casa-brightwell.example</p>
  <div class="kitchen-photo" role="img" aria-label="Photo of a remodeled kitchen with island, wood cabinets and hardwood floor"></div>
  <div class="steel-panel" role="img" aria-label="Brushed stainless steel surface"></div>
  <div class="contact">
    <p class="owner">Marcus Delane</p>
    <p class="credentials">Licensed and Insured</p>
    <p class="phone">904-555-0172</p>
    <p class="email">marcusdelane@example.com</p>
  </div>
  <div class="payments" aria-label="Accepted payment cards">
    <span class="card-name"><i></i>Paxa</span>
    <span class="card-name"><i></i>Orbita</span>
    <span class="card-name"><i></i>Amerin</span>
  </div>
</section>

</body>
</html>
```